Flyer Design Project

We are a start-up real estate brokerage looking to attract new agents. Our business relies heavily on technology to help give agents more time to spend with clients. Our model is also different from a typical broker in that we do not take a percentage of commission from each sale an agent makes. Instead we charge a simple flat monthly fee and the agent keeps 100% of the commission the earn.
The ideal flyer will be pleasing to the eye, should probably have some appropriate graphics, use our logo and project a modern yet sophisticated company image. This is and advertising flyer that will be followed up with a more detailed brochure (later project).
Updates

While I like the initial design I was looking for more of a change from my design.  Here are some clarifications:

The design should not included the "click" option so it can be used online or in print.  Instead include the site corvelliahomes.com/careers

I want more of a list of features with less description.  The list should have:
- Deal Tracker included
- No Commission Split
- No Floor Time... Leads sent directly to you
- E & O Insurance included
- All your listings showcased on Homefinda.com
- Showing appointment solution.

Some description of each can be included but less of a question answer style than what I originally had.
It does not need to be a straight list, the items all need to be mentioned somewhere on the flyer but not necessarily in a list style.
Maybe an image of business meeting or greeting (agent joining).

Please do not hesitate to ask questions for clarification

The image of meeting or greeting is optional - you choose what you think is best.
Also, use of the "About Us" that was uploaded my be a good idea.  - I'm not sure on this either

Target Market(s)

current real estate agents and people considering a real estate career

Industry/Entity Type

Real Estate

Requirements
Must have
• Should list that we include "Deal Tracker" which is considered the top program for real estate agents (info and logos can be found at dealtracker.com)
Should highlight our low cost structure ($350 per month) and no transaction fees.
Should highlight that no office time is required. We provide virtual office solutions to save time.
Our contact number (555) 482-9167 ext. 204
Nice to have
• Any other additional information from the attached flyers (which should not be used as a template as they all need to be designed in a later project).

```html
<!DOCTYPE html>
<html lang="en">
<head>
<meta charset="utf-8">
<title>Corvellia Homes – Agent Recruiting Flyer</title>
<link rel="stylesheet" href="https://fonts.googleapis.com/css2?family=EB+Garamond:wght@400;500;600;700&display=swap">
<style>
  :root {
    --crimson: #a3173a;
    --crimson-dark: #6e0c24;
    --ink: #1a1a1a;
    --grey-text: #8a8a8a;
    --paper: #ffffff;
    --backdrop: #e4e4e2;
    --plan: #ececec;
    --pill-shadow: rgba(0,0,0,0.28);
  }
  * { margin: 0; padding: 0; box-sizing: border-box; }
  html, body { width: 962px; height: 1200px; overflow: hidden; }
  body {
    background: var(--backdrop);
    font-family: "EB Garamond", Georgia, serif;
    position: relative;
  }
  .flyer {
    position: absolute; left: 52px; top: 42px;
    width: 866px; height: 1123px;
    background: var(--paper);
    box-shadow: 0 2px 8px rgba(0,0,0,0.35);
  }
  .hero-photo {
    position: absolute; left: 0; top: 0; width: 440px; height: 350px;
    background: linear-gradient(100deg, #24262b 0%, #3a3d44 35%, #c9c1b8 62%, #f4f1ee 85%, #ffffff 100%);
  }
  .brand { position: absolute; left: 410px; top: 150px; }
  .brand-dot {
    position: absolute; left: 0; top: 6px; width: 58px; height: 58px;
    border-radius: 50%; background: var(--crimson);
  }
  .brand-name {
    position: absolute; left: 98px; top: 0; white-space: nowrap;
    font-size: 46px; font-weight: 500; color: var(--ink); letter-spacing: 1px; line-height: 1;
  }
  .brand-rule {
    position: absolute; left: 98px; top: 52px; width: 308px; height: 1px; background: #9a9a9a;
  }
  .brand-sub {
    position: absolute; left: 100px; top: 60px; width: 306px;
    font-size: 17px; color: var(--grey-text); letter-spacing: 1px;
    display: flex; justify-content: space-between;
  }
  .about {
    position: absolute; left: 0; top: 351px; width: 866px; height: 169px;
    background: var(--crimson); color: #fff;
  }
  .about-title {
    position: absolute; left: 58px; top: 71px; font-size: 23px; font-weight: 500; letter-spacing: 0.5px;
  }
  .about-col {
    position: absolute; top: 30px; width: 242px;
    font-size: 13.2px; line-height: 14.6px; text-align: justify; font-weight: 500;
    hyphens: auto;
  }
  .about-col p { text-indent: 10px; }
  .about-col.first { left: 315px; }
  .about-col.second { left: 573px; }
  .gallery { position: absolute; top: 530px; height: 112px; }
  .gallery.one { left: 53px; width: 247px; background: linear-gradient(180deg, #bcd6ea 0%, #e8e6e0 55%, #7f8c74 100%); }
  .gallery.two { left: 309px; width: 247px; background: linear-gradient(180deg, #6f8f4e 0%, #c9cfc2 55%, #5f8a3a 100%); }
  .gallery.three { left: 566px; width: 248px; background: linear-gradient(180deg, #c8dcec 0%, #9a9a9c 55%, #6f9a56 100%); }
  .plan {
    position: absolute; left: 52px; top: 652px; width: 763px; height: 353px;
    background: var(--plan);
  }
  .feature {
    position: absolute; height: 33px; background: var(--paper);
    border-radius: 0 17px 17px 0;
    box-shadow: 0 3px 4px var(--pill-shadow);
    color: var(--crimson); font-size: 18.5px; font-weight: 600;
    line-height: 33px; text-transform: uppercase; white-space: nowrap;
  }
  .feature.right { border-radius: 17px 0 0 17px; }
  .check { position: absolute; width: 70px; height: 50px; overflow: visible; }
  .price-badge {
    position: absolute; left: 99px; top: 819px; width: 150px; height: 150px;
    border-radius: 50%; background: var(--crimson); color: #fff;
    box-shadow: 0 3px 6px rgba(0,0,0,0.35);
  }
  .price-badge span { position: absolute; white-space: nowrap; font-weight: 600; line-height: 1; }
  .pb-label { left: 20px; top: 26px; font-size: 10px; }
  .pb-amount { left: 26px; top: 37px; font-size: 29px; }
  .pb-period { left: 41px; top: 70px; font-size: 14px; }
  .pb-no { left: 70px; top: 86px; font-size: 31px; }
  .pb-fees { left: 30px; top: 116px; font-size: 10px; }
  .call {
    position: absolute; left: 180px; top: 1030px; display: flex; align-items: center; gap: 14px;
    color: var(--crimson); font-size: 28px; font-weight: 600; white-space: nowrap;
  }
</style>
</head>
<body>
<svg width="0" height="0" style="position:absolute">
  <defs>
    <radialGradient id="ball" cx="35%" cy="35%" r="70%">
      <stop offset="0" stop-color="#d24a69"/>
      <stop offset="0.55" stop-color="#a3173a"/>
      <stop offset="1" stop-color="#5a0718"/>
    </radialGradient>
    <symbol id="tick-ball" viewBox="0 0 70 50">
      <circle cx="22" cy="28" r="20" fill="url(#ball)"/>
      <path d="M12 30 L22 38 L66 6" fill="none" stroke="#111" stroke-width="2.4" stroke-linecap="round" stroke-linejoin="round"/>
    </symbol>
  </defs>
</svg>

<main class="flyer">
  <div class="hero-photo" role="img" aria-label="Agent in a dark suit holding a small model house on an open hand"></div>

  <div class="brand">
    <div class="brand-dot"></div>
    <div class="brand-name">CORVELLIA</div>
    <div class="brand-rule"></div>
    <div class="brand-sub"><span>H</span><span>O</span><span>M</span><span>E</span><span>S</span></div>
  </div>

  <section class="about" lang="en">
    <h2 class="about-title">ABOUT US</h2>
    <div class="about-col first">
      <p>Corvellia Homes is a boutique real estate firm specializing in residential properties on Long Island.</p>
      <p>Here at Corvellia Homes we focus on providing the personalized customer service associated with a traditional brick and mortar real estate firms while employing the latest technology to efficiently and effectively rep-</p>
    </div>
    <div class="about-col second">
      resent our clients at the lowest possible cost. With over 90% of home buyers searching online we saw a need to update the traditional brokerage model with a better balance of technology and service. Our company is founded on the belief that the use of technology can actually increase the quality of customer service in the real estate business.
    </div>
  </section>

  <div class="gallery one" role="img" aria-label="Modern two-storey white house with stone accents"></div>
  <div class="gallery two" role="img" aria-label="Single-storey modern home among tall trees and lawn"></div>
  <div class="gallery three" role="img" aria-label="Contemporary family house with driveway and palm trees"></div>

  <div class="plan" role="img" aria-label="Faint architectural floor plan with master bedroom, bathroom, linen and laundry rooms"></div>

  <div class="feature" style="left:8px; top:670px; width:363px; padding-left:108px;">Deal Tracker included</div>
  <svg class="check" style="left:36px; top:660px;"><use href="#tick-ball"/></svg>

  <div class="feature" style="left:0; top:718px; width:618px; padding-left:159px;">No floor time... leads sent directly to you</div>
  <svg class="check" style="left:76px; top:708px;"><use href="#tick-ball"/></svg>

  <div class="feature" style="left:0; top:768px; width:408px; padding-left:176px;">No commission split</div>
  <svg class="check" style="left:111px; top:758px;"><use href="#tick-ball"/></svg>

  <div class="feature right" style="left:380px; top:818px; width:486px; padding-left:29px;">E &amp; O insurance included</div>
  <svg class="check" style="left:734px; top:807px;"><use href="#tick-ball"/></svg>

  <div class="feature right" style="left:240px; top:870px; width:626px; padding-left:20px;">All your listings showcased on Homefinda.com</div>
  <svg class="check" style="left:788px; top:859px;"><use href="#tick-ball"/></svg>

  <div class="feature right" style="left:323px; top:916px; width:543px; padding-left:42px;">Showing appointment solution.</div>
  <svg class="check" style="left:724px; top:905px;"><use href="#tick-ball"/></svg>

  <div class="price-badge">
    <span class="pb-label">LOW COST STRUCTURE</span>
    <span class="pb-amount">$350</span>
    <span class="pb-period">PER MONTH</span>
    <span class="pb-no">NO</span>
    <span class="pb-fees">TRANSACTION FEES</span>
  </div>

  <div class="call">
    <svg width="20" height="46" viewBox="0 0 20 46" aria-hidden="true">
      <path d="M14 1 C6 3 2 12 2 23 C2 34 6 43 14 45 L18 42 L13 31 L9 32 C7 27 7 19 9 14 L13 15 L18 4 Z" fill="var(--crimson)"/>
    </svg>
    <span>CALL NOW : (555) 482-9167 ext. 204</span>
  </div>
</main>
</body>
</html>
```